Business card with logo and words.

Colours: aqua and white (but open to suggestions).
Double sided card ok.
Need to convey competence, calmness, listening skills
Words:
Quiet Harbour Care Guidance
Ruth Pemberly
RN, RM, MQDNS, Grad Dip Gr & Pall Care Couns, Grad Cert Pall Care in Aged Care
quietharbourcg@mailvane.net

```html
<!DOCTYPE html>
<html lang="en">
<head>
<meta charset="utf-8">
<title>Quiet Harbour Care Guidance – Business Card</title>
<link href="https://fonts.googleapis.com/css2?family=Montserrat:wght@300;400;600;700&display=swap" rel="stylesheet">
<style>
  :root {
    --violet: #3a2a85;
    --aqua: #86cba0;
    --crimson: #e0103f;
    --paper: #ffffff;
    --edge: #111111;
  }
  html, body {
    margin: 0;
    padding: 0;
    width: 1020px;
    height: 1200px;
    overflow: hidden;
    background: var(--paper);
    font-family: "Montserrat", sans-serif;
  }
  .canvas {
    position: relative;
    width: 1020px;
    height: 1200px;
  }
  .card-front {
    position: absolute;
    left: 0; top: 0;
    width: 1020px; height: 565px;
  }
  .rays {
    position: absolute;
    inset: 0;
    background: radial-gradient(ellipse at 34% 46%, var(--aqua) 0%, #5f8fa0 45%, var(--violet) 100%);
  }
  .brand {
    position: absolute;
    display: flex;
    align-items: center;
    gap: 18px;
    color: var(--paper);
    font-weight: 700;
    text-transform: uppercase;
    line-height: 1.1;
  }
  .brand-dot {
    flex: none;
    border-radius: 50%;
    background: var(--paper);
  }
  .card-front .brand {
    left: 90px; top: 200px;
    width: 560px;
    font-size: 50px;
  }
  .card-front .brand-dot { width: 70px; height: 70px; }

  .card-back {
    position: absolute;
    left: 0; top: 632px;
    width: 1018px; height: 566px;
    border: 1px solid var(--edge);
    background: var(--violet);
    overflow: hidden;
  }
  .back-badge {
    position: absolute;
    left: 0; top: 0;
    width: 438px; height: 245px;
  }
  .card-back .brand {
    left: 34px; top: 76px;
    width: 380px;
    font-size: 28px;
    gap: 12px;
  }
  .card-back .brand-dot { width: 40px; height: 40px; }

  .holder-name {
    position: absolute;
    right: 52px; top: 180px;
    margin: 0;
    color: var(--paper);
    font-weight: 600;
    font-size: 50px;
    letter-spacing: 0.5px;
  }
  .credentials {
    position: absolute;
    right: 52px; top: 272px;
    margin: 0;
    color: var(--paper);
    font-weight: 300;
    font-size: 29px;
    line-height: 42px;
    text-align: right;
  }
  .email-band {
    position: absolute;
    left: 36px; top: 424px;
    width: 982px; height: 46px;
    background: linear-gradient(90deg, var(--violet) 0%, #2f5aa0 12%, var(--paper) 32%, var(--paper) 100%);
  }
  .email {
    position: absolute;
    right: 40px; top: 0;
    color: var(--crimson);
    font-weight: 600;
    font-size: 36px;
    line-height: 46px;
  }
  .accent-strip {
    position: absolute;
    left: 160px; top: 478px;
    width: 858px; height: 22px;
    background: linear-gradient(90deg, var(--violet) 0%, var(--aqua) 30%, var(--aqua) 100%);
  }
</style>
</head>
<body>
<div class="canvas">
  <section class="card-front">
    <div class="rays" role="img" aria-label="Sunburst of violet and aqua rays radiating from the emblem"></div>
    <div class="brand">
      <span class="brand-dot"></span>
      <span class="brand-name">Quiet Harbour Care Guidance</span>
    </div>
  </section>

  <section class="card-back">
    <div class="back-badge rays" role="img" aria-label="Sunburst of violet and aqua rays behind the emblem"></div>
    <div class="brand">
      <span class="brand-dot"></span>
      <span class="brand-name">Quiet Harbour Care Guidance</span>
    </div>
    <h1 class="holder-name">Ruth Pemberly</h1>
    <p class="credentials">RN, RM, MQDNS,<br>Grad Dip Gr &amp; Pall Care Couns,<br>Grad Cert Pall Care in Aged Care</p>
    <div class="email-band">
      <span class="email">quietharbourcg@mailvane.net</span>
    </div>
    <div class="accent-strip"></div>
  </section>
</div>
</body>
</html>
```